Graduation Yearbook Page for a Young Lady

A one page for my daughter's yearbook. She is in 8th grade, which in her school is the year they graduate and go to different highschools. I am looking for a clean and elegant and yet imaginative layout that incorporates "Nola, Congratulations, We are so very proud of you. Mom, Dad, Grandma, Gwen and Desmond.
Please feel free as many or as few as 4 of the attached photos. The main photo Nola Smiling should be in the center.

```html
<!DOCTYPE html>
<html lang="en">
<head>
<meta charset="utf-8">
<title>Nola – Graduation Yearbook Page</title>
<link rel="stylesheet" href="https://fonts.googleapis.com/css2?family=Montserrat:wght@600&family=Tinos:ital@0;1&display=swap">
<style>
  :root {
    --paper: #ffffff;
    --ink: #000000;
    --frame: #bdbdbd;
    --band-light: #ededed;
    --band-mid: #d4d4d4;
    --oval-ring: #d8d8d8;
    --portrait-dark: #3a3a3a;
    --portrait-light: #f4f4f4;
  }
  html, body {
    margin: 0;
    padding: 0;
    width: 1200px;
    height: 900px;
    overflow: hidden;
    background: var(--paper);
  }
  .page {
    position: relative;
    width: 1200px;
    height: 900px;
  }
  .page-art {
    display: block;
    width: 1200px;
    height: 900px;
  }
  .band-light { fill: var(--band-light); }
  .band-mid { fill: var(--band-mid); }
  .page-frame { fill: none; stroke: var(--frame); stroke-width: 1.5; }
  .name-block { fill: var(--ink); }
  .name-letters {
    fill: var(--paper);
    font-family: "Montserrat", sans-serif;
    font-weight: 600;
    font-size: 172px;
    letter-spacing: -6px;
  }
  .message-oval { fill: var(--paper); stroke: var(--oval-ring); stroke-width: 9; }
  .message-title {
    font-family: "Tinos", serif;
    font-size: 50px;
    fill: var(--ink);
  }
  .message-line {
    font-family: "Tinos", serif;
    font-size: 24px;
    fill: var(--ink);
  }
  .message-signature {
    font-family: "Tinos", serif;
    font-style: italic;
    font-size: 17px;
    fill: var(--ink);
  }
</style>
</head>
<body>
<main class="page">
  <svg class="page-art" viewBox="0 0 1200 900" xmlns="http://www.w3.org/2000/svg">
    <defs>
      <linearGradient id="portrait-tone" x1="0" y1="0" x2="0" y2="1">
        <stop offset="0" stop-color="var(--portrait-dark)"/>
        <stop offset="0.7" stop-color="#8a8a8a"/>
        <stop offset="1" stop-color="var(--portrait-light)"/>
      </linearGradient>
    </defs>

    <!-- background bands -->
    <g class="background-bands">
      <rect class="band-light" x="96" y="62" width="1009" height="18"/>
      <rect class="band-light" x="96" y="140" width="1009" height="28"/>
      <rect class="band-light" x="96" y="222" width="1009" height="28"/>
      <rect class="band-mid" x="852" y="62" width="28" height="780"/>
      <rect class="band-mid" x="960" y="62" width="28" height="780"/>
      <rect class="band-mid" x="1020" y="62" width="26" height="780"/>
    </g>

    <!-- portrait area -->
    <path class="portrait" role="img" aria-label="Portrait of Nola formed from repeated lettering 'We love you Nola'"
          fill="url(#portrait-tone)"
          d="M150 842 L150 520 Q150 440 210 400 L230 120 Q260 66 360 64 Q470 66 495 120 L520 400 Q600 450 640 520 L640 842 Z"/>

    <!-- name block -->
    <rect class="name-block" x="838" y="92" width="224" height="332"/>
    <text class="name-letters" x="838" y="246" textLength="224" lengthAdjust="spacingAndGlyphs">NO</text>
    <text class="name-letters" x="838" y="420" textLength="224" lengthAdjust="spacingAndGlyphs">LA</text>

    <!-- message -->
    <ellipse class="message-oval" cx="875" cy="690" rx="232" ry="128"/>
    <text class="message-title" x="875" y="683" text-anchor="middle">Congratulations,</text>
    <text class="message-line" x="875" y="717" text-anchor="middle">We are so very proud of you!</text>
    <text class="message-signature" x="875" y="747" text-anchor="middle">Mom, Dad, Grandma, Gwen and Desmond.</text>

    <rect class="page-frame" x="96" y="62" width="1009" height="780"/>
  </svg>
</main>
</body>
</html>
```